Digital One Pager for Consulting Practice

I would like the essence of the content in my ppt consolidated into a one-pager. The one-pager will mainly be sent via email as a pdf and intended to excite and invite new clients and establish the credibility of my boutique high-end consulting firm. Infographics and symbols would be a plus. The target client should view the firm as providing premeir service. The client is getting a thought partner.

Target Market(s)

Large Medical Device Manufacturer Executives, Early-Stage Medical Device Manufacturer Executives, Partners at VC Firms

Industry/Entity Type

Medical Equipment

Colors
0355a3
f37122

Requirements
Must have
• Please match the color scheme in ppt. Please use the existing logo. I am very open to better graphics on the process. My photo does not need to be on the digital flyer. Hyper link to the website and email is needed.
Nice to have
• Infographics

```html
<!DOCTYPE html>
<html lang="en">
<head>
<meta charset="utf-8">
<title>Harlow Ventures – One Pager</title>
<link href="https://fonts.googleapis.com/css2?family=Carlito:wght@400;700&family=Tinos&family=Montserrat:wght@500&display=swap" rel="stylesheet">
<style>
  :root{
    --navy:#111b33;
    --orange:#f37122;
    --orange-dark:#e0621a;
    --panel:#f2f2f3;
    --ink:#2a2f3a;
    --muted:#7b7f86;
    --white:#ffffff;
  }
  *{margin:0;padding:0;box-sizing:border-box}
  html,body{width:959px;height:1200px;overflow:hidden;background:#fff}
  body{font-family:"Carlito",Calibri,sans-serif;color:var(--ink);position:relative}
  .header{position:absolute;left:0;top:0;width:959px;height:164px;background:var(--white)}
  .brand{position:absolute;left:30px;top:54px;display:flex;align-items:center;gap:14px;
    font-family:"Montserrat",sans-serif;font-weight:500;font-size:40px;letter-spacing:5px;color:var(--navy)}
  .brand-mark{width:34px;height:34px;background:var(--orange)}
  .value-band{position:absolute;left:0;top:164px;width:959px;height:266px;background:var(--navy)}
  .value-title{position:absolute;left:28px;top:44px;font-family:"Tinos",serif;font-size:52px;color:var(--orange);letter-spacing:1px}
  .value-list{position:absolute;left:30px;top:118px;width:900px;list-style:none;display:grid;grid-template-columns:470px 430px;row-gap:16px}
  .value-list li{display:flex;align-items:center;gap:16px;font-size:37px;color:var(--white);letter-spacing:.5px}
  .value-list svg{flex:none}
  .services{position:absolute;left:0;top:430px;width:509px;height:687px;background:var(--white)}
  .details{position:absolute;left:509px;top:430px;width:450px;height:687px;background:var(--panel);padding:62px 30px 0 34px}
  .section-title{font-family:"Tinos",serif;font-size:25px;color:var(--orange);font-weight:400}
  .group-title{font-size:17px;color:var(--ink);margin-top:8px}
  .bullets{list-style:none;margin-top:6px}
  .bullets li{position:relative;padding-left:26px;font-size:16px;color:var(--muted);line-height:19px;margin-bottom:9px}
  .bullets li::before{content:"";position:absolute;left:2px;top:3px;width:11px;height:11px;border:1.4px solid var(--muted);border-radius:50%}
  .bullets li::after{content:"";position:absolute;left:6px;top:7px;width:3px;height:3px;border-right:1.4px solid var(--muted);border-bottom:1.4px solid var(--muted);transform:rotate(-45deg)}
  .process{margin-top:44px}
  .steps{display:flex;justify-content:space-between;margin-top:18px;width:375px}
  .step{width:90px;text-align:center;font-size:12px;line-height:13px;color:var(--muted);text-transform:uppercase}
  .step-icon{width:62px;height:62px;margin:0 auto 10px;border-radius:50%;background:var(--orange);box-shadow:0 3px 4px rgba(0,0,0,.2);display:flex;align-items:center;justify-content:center}
  .partners{margin-top:42px}
  .partners h3{font-size:17px;font-weight:400;color:var(--ink)}
  .badges{display:flex;flex-wrap:wrap;gap:8px 10px;margin-top:8px;width:370px;align-items:center}
  .badge{height:24px;background:#c9ccd3}
  .badge.dark{background:var(--navy)}
  .badge.blue{background:#0355a3}
  .footer-phone{position:absolute;left:0;top:1117px;width:457px;height:83px;background:var(--navy);display:flex;align-items:center;justify-content:center;gap:20px;color:var(--white);font-size:37px}
  .footer-links{position:absolute;left:457px;top:1117px;width:502px;height:83px;background:var(--orange);display:flex;align-items:center;justify-content:center;gap:10px;color:var(--white);font-size:18px}
  .footer-links a{color:var(--white);text-decoration:none}
</style>
</head>
<body>
  <header class="header">
    <div class="brand"><span class="brand-mark"></span>HARLOW VENTURES</div>
  </header>

  <section class="value-band">
    <h1 class="value-title">VALUE</h1>
    <ul class="value-list">
      <li><svg width="26" height="26" viewBox="0 0 26 26"><rect x="2" y="5" width="19" height="19" rx="3" fill="none" stroke="#f37122" stroke-width="2.5"/><path d="M7 14l4 4 12-14" fill="none" stroke="#f37122" stroke-width="2.8"/></svg>Extensive Experience</li>
      <li><svg width="26" height="26" viewBox="0 0 26 26"><rect x="2" y="5" width="19" height="19" rx="3" fill="none" stroke="#f37122" stroke-width="2.5"/><path d="M7 14l4 4 12-14" fill="none" stroke="#f37122" stroke-width="2.8"/></svg>Valued Network</li>
      <li><svg width="26" height="26" viewBox="0 0 26 26"><rect x="2" y="5" width="19" height="19" rx="3" fill="none" stroke="#f37122" stroke-width="2.5"/><path d="M7 14l4 4 12-14" fill="none" stroke="#f37122" stroke-width="2.8"/></svg>Efficient Process</li>
      <li><svg width="26" height="26" viewBox="0 0 26 26"><rect x="2" y="5" width="19" height="19" rx="3" fill="none" stroke="#f37122" stroke-width="2.5"/><path d="M7 14l4 4 12-14" fill="none" stroke="#f37122" stroke-width="2.8"/></svg>Regulatory Strategy</li>
    </ul>
  </section>

  <section class="services">
    <svg width="509" height="687" viewBox="0 0 509 687" font-family="Carlito, Calibri, sans-serif" text-anchor="middle">
      <g fill="#f37122" stroke="#fff" stroke-width="4">
        <polygon points="34,186 97,80 225,80 288,186 225,292 97,292"/>
        <polygon points="227,293 290,187 418,187 481,293 418,399 290,399"/>
        <polygon points="34,399 97,293 225,293 288,399 225,505 97,505"/>
        <polygon points="227,505 290,399 418,399 481,505 418,611 290,611"/>
      </g>
      <g fill="#fff" stroke="#c9ccd3" stroke-width="3">
        <circle cx="161" cy="112" r="33"/>
        <circle cx="354" cy="219" r="33"/>
        <circle cx="161" cy="325" r="33"/>
        <circle cx="354" cy="431" r="33"/>
      </g>
      <g fill="#111b33">
        <rect x="146" y="112" width="5" height="14"/><rect x="154" y="106" width="5" height="20"/><rect x="162" y="100" width="5" height="26"/><rect x="170" y="94" width="5" height="32"/>
        <path d="M144 104l10-8 8 5 14-12" fill="none" stroke="#111b33" stroke-width="2.5"/>
        <rect x="342" y="200" width="22" height="30" rx="1"/>
        <rect x="346" y="206" width="14" height="2" fill="#fff"/><rect x="346" y="211" width="14" height="2" fill="#fff"/><rect x="346" y="216" width="14" height="2" fill="#fff"/><rect x="346" y="221" width="14" height="2" fill="#fff"/>
        <circle cx="161" cy="315" r="7"/><rect x="150" y="323" width="22" height="10" rx="4"/>
        <path d="M161 333v8M143 327h36" stroke="#111b33" stroke-width="2" fill="none"/>
        <circle cx="143" cy="327" r="3"/><circle cx="179" cy="327" r="3"/><circle cx="161" cy="343" r="3"/>
        <rect x="342" y="416" width="20" height="28" rx="2" fill="none" stroke="#111b33" stroke-width="2.5"/>
        <rect x="346" y="423" width="12" height="2"/><rect x="346" y="429" width="12" height="2"/><rect x="346" y="435" width="8" height="2"/>
        <path d="M357 444l13-16" stroke="#111b33" stroke-width="3"/>
      </g>
      <g fill="#fff">
        <text x="161" y="180" font-size="17">REGULATORY</text>
        <text x="161" y="202" font-size="17">STRATEGY</text>
        <text x="161" y="226" font-size="13">RAQA Organizational Structure</text>
        <text x="161" y="243" font-size="13">Regulatory Pathway</text>
        <text x="354" y="286" font-size="17">FDA</text>
        <text x="354" y="308" font-size="17">COMMUNICATIONS</text>
        <text x="354" y="332" font-size="13">Deficiency Response</text>
        <text x="354" y="349" font-size="13">Application Review</text>
        <text x="161" y="392" font-size="17">INTERIM</text>
        <text x="161" y="414" font-size="17">EXECUTIVE LEADERSHIP</text>
        <text x="161" y="438" font-size="13">Compliance Remediation</text>
        <text x="161" y="455" font-size="13">Accelerated Product</text>
        <text x="161" y="472" font-size="13">Registration</text>
        <text x="354" y="509" font-size="17">TRAINING</text>
        <text x="354" y="533" font-size="13">FDA Communication</text>
        <text x="354" y="550" font-size="13">MDR Reporting</text>
      </g>
    </svg>
  </section>

  <section class="details">
    <h2 class="section-title">Experience to Provide...</h2>
    <h3 class="group-title">Executive Application Review</h3>
    <ul class="bullets">
      <li>Examples include: Presubmission, IDE, 510(k), 513(g), PMA, Refuse to Accept, Hold letter</li>
      <li>Troubleshooting</li>
    </ul>
    <h3 class="group-title" style="margin-top:14px">Strategic Advice &amp; Diligence to Investors</h3>
    <ul class="bullets">
      <li>Validate &amp; Verify Founder Milestones</li>
      <li>Diligence portfolio company Regulatory and Quality systems</li>
    </ul>

    <div class="process">
      <h2 class="section-title">Efficient Process</h2>
      <div class="steps">
        <div class="step"><div class="step-icon"><svg width="30" height="30" viewBox="0 0 30 30"><path d="M9 12a6 6 0 0 1 12 0v3M7 13h3v6H7zM20 13h3v6h-3z" fill="#fff" stroke="#fff" stroke-width="1.5"/><rect x="9" y="21" width="12" height="7" rx="3" fill="#fff"/></svg></div>Exploratory Call</div>
        <div class="step"><div class="step-icon"><svg width="30" height="30" viewBox="0 0 30 30"><rect x="6" y="4" width="15" height="21" fill="none" stroke="#fff" stroke-width="2"/><path d="M9 9h9M9 13h6" stroke="#fff" stroke-width="2"/><circle cx="19" cy="19" r="4" fill="none" stroke="#fff" stroke-width="2"/><path d="M22 22l4 4" stroke="#fff" stroke-width="2.5"/></svg></div>Regulatory Landscape</div>
        <div class="step"><div class="step-icon"><svg width="30" height="30" viewBox="0 0 30 30"><circle cx="15" cy="12" r="7" fill="#fff"/><rect x="12" y="19" width="6" height="6" fill="#fff"/></svg></div>Problem Statement</div>
        <div class="step"><div class="step-icon"><svg width="30" height="30" viewBox="0 0 30 30"><circle cx="11" cy="17" r="6" fill="none" stroke="#fff" stroke-width="3.5" stroke-dasharray="3 2"/><circle cx="21" cy="9" r="4" fill="none" stroke="#fff" stroke-width="3" stroke-dasharray="2.5 1.5"/></svg></div>Review &amp; Align on Deliverables</div>
      </div>
    </div>

    <div class="partners">
      <h3>Valued Partner Network</h3>
      <div class="badges">
        <span class="badge" style="width:210px"></span>
        <span class="badge" style="width:44px"></span>
        <span class="badge dark" style="width:58px;height:26px"></span>
        <span class="badge" style="width:58px"></span>
        <span class="badge blue" style="width:46px"></span>
        <span class="badge" style="width:58px"></span>
      </div>
    </div>
  </section>

  <footer>
    <div class="footer-phone">
      <svg width="32" height="32" viewBox="0 0 32 32"><circle cx="16" cy="16" r="14" fill="none" stroke="#fff" stroke-width="2.5"/><path d="M11 9l3 0 1.5 4-2 1.5a9 9 0 0 0 4 4l1.5-2 4 1.5 0 3c-6 1-13-6-12-12z" fill="#fff"/></svg>
      <span>555.014.2290</span>
    </div>
    <div class="footer-links">
      <a href="https://www.harlowventures.com">www.harlowventures.com</a>
      <span>|</span>
      <a href="mailto:info@harlowventures.com">info@harlowventures.com</a>
    </div>
  </footer>
</body>
</html>
```